Copper Kettle Catering Menu

Design 1 page (double sided is ok) menu for catering company.

A flat non-folding menu. Letter paper sized.
Updates

I'm having trouble adding attachments via Drafting Hive.  I have contacted Drafting Hive and will hopefully have them up soon.  

Industry/Entity Type

Catering

Font styles to use
Serif

Requirements
Must have
• Copper Kettle Catering logo

menu items from attachment

Double sided is ok

```html
<!DOCTYPE html>
<html lang="en">
<head>
<meta charset="utf-8">
<title>Copper Kettle Catering – Menu Back Page</title>
<link href="https://fonts.googleapis.com/css2?family=Tinos:wght@400;700&display=swap" rel="stylesheet">
<style>
  :root {
    --backdrop: #e4e4e4;
    --paper: #ffffff;
    --ink: #111111;
    --ink-soft: #5e5e5e;
    --accent: #6fb1e3;
    --footer-ink: #7d8b97;
  }
  * { box-sizing: border-box; margin: 0; padding: 0; }
  html, body { width: 1200px; height: 1000px; overflow: hidden; }
  body {
    background: var(--backdrop);
    font-family: "Tinos", "Times New Roman", serif;
    color: var(--ink);
    position: relative;
  }
  .menu-page {
    position: absolute; left: 235px; top: 28px;
    width: 730px; height: 944px;
    background: var(--paper);
  }
  .top-rule, .bottom-rule {
    position: absolute; left: 42px; width: 643px; height: 1px;
    background: var(--accent);
  }
  .top-rule { top: 57px; }
  .bottom-rule { top: 877px; }

  .column { position: absolute; top: 91px; }
  .column-left { left: 84px; width: 265px; }
  .column-right { left: 379px; width: 266px; }

  .section-title {
    font-size: 15px; font-weight: 700; text-align: center;
    line-height: 18px; margin-bottom: 8px;
  }
  .item { margin-bottom: 10px; }
  .item-line {
    display: flex; align-items: baseline;
    font-size: 11.3px; font-weight: 700; line-height: 18px;
  }
  .leader {
    flex: 1; margin: 0 4px;
    border-bottom: 1px dotted #333;
    transform: translateY(-3px);
  }
  .details { list-style: none; }
  .details li {
    position: relative; padding-left: 18px;
    font-size: 11px; line-height: 14.5px; color: var(--ink-soft);
    letter-spacing: 0.2px; word-spacing: 1.5px;
  }
  .details li::before {
    content: ""; position: absolute; left: 6px; top: 5px;
    width: 4px; height: 4px; border-radius: 50%;
    background: var(--accent); opacity: 0.7;
  }
  .note { font-size: 11px; color: var(--ink-soft); line-height: 16px; }

  .divider {
    display: flex; align-items: center; justify-content: center;
    gap: 2px; margin: 12px 0 9px;
  }
  .divider::before, .divider::after {
    content: ""; width: 46px; height: 1px; background: var(--accent);
  }
  .divider span { color: var(--accent); font-size: 9px; line-height: 9px; }

  .price-list .item-line { line-height: 18px; }
  .platter { margin-bottom: 10px; }
  .platter-name { font-size: 11.3px; font-weight: 700; line-height: 18px; margin-bottom: 2px; }
  .size-rows { list-style: none; width: 213px; }
  .size-rows li {
    position: relative; padding-left: 18px;
    display: flex; align-items: baseline;
    font-size: 11px; line-height: 14.3px; color: var(--ink-soft);
  }
  .size-rows li::before {
    content: ""; position: absolute; left: 6px; top: 5px;
    width: 4px; height: 4px; border-radius: 50%;
    background: var(--accent); opacity: 0.7;
  }
  .size-rows .leader { border-bottom-color: #888; }

  .contact-bar {
    position: absolute; left: 42px; top: 886px; width: 643px;
    display: flex; justify-content: space-between; align-items: baseline;
    font-size: 13.5px; color: var(--footer-ink); letter-spacing: 0.3px;
  }
  .contact-bar b { font-weight: 700; }
  .contact-bar .dot { color: var(--accent); font-size: 10px; }
</style>
</head>
<body>
<main class="menu-page">
  <div class="top-rule"></div>

  <section class="column column-left">
    <h2 class="section-title">Salads</h2>
    <div class="item">
      <div class="item-line"><span>Greek Salad</span><span class="leader"></span><span>$8.99 per guest</span></div>
      <ul class="details"><li>Mixed Greens, Green Peppers, Kalamato Olives, Feta Cheese, Tomatoes, Greek Peppers Greek Dressing</li></ul>
    </div>
    <div class="item">
      <div class="item-line"><span>Grilled Chicken Salad</span><span class="leader"></span><span>$9.99 per guest</span></div>
      <ul class="details"><li>Grilled Chicken, Roquefort Cheese, and Walnuts with Mixed Greens Balsamic Dressing</li></ul>
    </div>
    <div class="item">
      <div class="item-line"><span>Chicken Caesar Salad</span><span class="leader"></span><span>$9.99 per guest</span></div>
      <ul class="details"><li>Marinated Chicken, Romaine Lettuce, Croutons Creamy Caesar Dressing</li></ul>
    </div>
    <div class="item">
      <div class="item-line"><span>Antipasto Salad</span><span class="leader"></span><span>$9.99 per guest</span></div>
      <ul class="details"><li>Mixed Greens, Ham, Salami, Provolone Cheese, Peppers and Olives Italian Dressing</li></ul>
    </div>
    <div class="item">
      <div class="item-line"><span>Chef Salad</span><span class="leader"></span><span>$9.99 per guest</span></div>
      <ul class="details"><li>Mixed Greens, Turkey, Ham, Cheese, Egg, Tomatoes, Cucumbers, Carrots, Choice of Dressing</li></ul>
    </div>

    <div class="divider"><span>✻</span></div>

    <h2 class="section-title">Hot Lunch Buffets</h2>
    <div class="item">
      <div class="item-line"><span>All American Booster Buffet</span><span class="leader"></span><span>$10.99 per guest</span></div>
      <ul class="details">
        <li>Choice of Turkey, Roast Beef or Ham</li>
        <li>Mashed Potatoes or Rice,</li>
        <li>Gravy, Rolls, Tossed Green Salad,</li>
        <li>Cookies or Brownies</li>
      </ul>
    </div>
    <div class="item">
      <div class="item-line"><span>Tour of Italy - Italian Buffet</span><span class="leader"></span><span>$10.99 Per Guest</span></div>
      <ul class="details">
        <li>Choice of Two: Lasagna, Baked Ziti, Fettuccini Alfredo</li>
        <li>Meatballs or Italian Sausage</li>
        <li>Tossed Green Salad, Garlic Bread</li>
        <li>Cookies or Brownies</li>
      </ul>
    </div>
    <div class="item">
      <div class="item-line"><span>Chicken Marsala Bar</span><span class="leader"></span><span>$10.99 Per Guest</span></div>
      <ul class="details">
        <li>Chicken Marsala</li>
        <li>Rice Pilaf, Vegetable Medley, Rolls, Tossed Green Salad</li>
        <li>Cookies or Brownies</li>
      </ul>
    </div>
    <div class="item">
      <div class="item-line"><span>Mexican Fiesta Bar</span><span class="leader"></span><span>$10.99 Per Guest</span></div>
      <ul class="details">
        <li>Soft Taco Shells with Tortilla Chips, Seasoned Beef, Refried Beans Yellow Rice, Diced Tomatoes, Onions, Shredded Lettuce, Cheese</li>
        <li>Sour Cream and Salsa</li>
        <li>Cookies or Brownies</li>
      </ul>
    </div>
    <div class="item">
      <div class="item-line"><span>Custom Gourmet Pizzas</span><span class="leader"></span><span>Starting at $9.99</span></div>
    </div>
  </section>

  <section class="column column-right">
    <h2 class="section-title">Snacks</h2>
    <div class="item">
      <div class="item-line"><span>Baked Goods</span><span class="leader"></span><span>$4.99 Per Guest</span></div>
      <ul class="details"><li>Assorted Cookies and Brownies</li><li>Bottle Water or Can Soda</li></ul>
    </div>
    <div class="item">
      <div class="item-line"><span>Sweet &amp; Salty</span><span class="leader"></span><span>$4.99 Per Guest</span></div>
      <ul class="details"><li>Assorted Candy Bars, Popcorn, Assorted Chips</li><li>Bottle Water or Can Soda</li></ul>
    </div>

    <div class="divider"><span>✻</span></div>

    <h2 class="section-title">A La Carte</h2>
    <div class="price-list">
      <div class="item-line"><span>Gourmet Cookies and Brownies</span><span class="leader"></span><span>$1.00 each</span></div>
      <div class="item-line"><span>Candy Bars</span><span class="leader"></span><span>$1.50 each</span></div>
      <div class="item-line"><span>Bag of Chips or Pretzels</span><span class="leader"></span><span>$1.25 each</span></div>
    </div>

    <div class="divider"><span>✻</span></div>

    <h2 class="section-title">Anytime Platters</h2>
    <ul class="details platter">
      <li>Small feeds 8-10</li><li>Medium feeds 16-20</li><li>Large feeds 26-30</li>
    </ul>
    <div class="platter">
      <h3 class="platter-name">Vegetable &amp; Dip Platter</h3>
      <ul class="size-rows">
        <li><span>Small</span><span class="leader"></span><span>$24.99</span></li>
        <li><span>Medium</span><span class="leader"></span><span>$39.99</span></li>
        <li><span>Large</span><span class="leader"></span><span>$59.99</span></li>
      </ul>
    </div>
    <div class="platter">
      <h3 class="platter-name">Cheese and Crackers Platter</h3>
      <ul class="size-rows">
        <li><span>Small</span><span class="leader"></span><span>$34.99</span></li>
        <li><span>Medium</span><span class="leader"></span><span>$49.99</span></li>
        <li><span>Large</span><span class="leader"></span><span>$69.99</span></li>
      </ul>
    </div>
    <div class="platter">
      <h3 class="platter-name">Fresh Fruit Platter</h3>
      <ul class="size-rows">
        <li><span>Small</span><span class="leader"></span><span>$24.99</span></li>
        <li><span>Medium</span><span class="leader"></span><span>$39.99</span></li>
        <li><span>Large</span><span class="leader"></span><span>$59.99</span></li>
      </ul>
    </div>
    <div class="platter">
      <h3 class="platter-name">Chicken Wing Platter</h3>
      <p class="note">(call for prices)</p>
    </div>

    <div class="divider"><span>✻</span></div>

    <h2 class="section-title">Beverages</h2>
    <div class="price-list">
      <div class="item-line"><span>Coffee</span><span class="leader"></span><span>$17.99 per gallon</span></div>
      <div class="item-line"><span>Orange Juice</span><span class="leader"></span><span>$13.99 per gallon</span></div>
      <div class="item-line"><span>Lemonade, Fruit Punch or Tea</span><span class="leader"></span><span>$11.99 per gallon</span></div>
      <div class="item-line"><span>Assorted Hot Tea</span><span class="leader"></span><span>$0.99 each</span></div>
      <div class="item-line"><span>Bottled Water</span><span class="leader"></span><span>$1.49 each</span></div>
      <div class="item-line"><span>Can Soda</span><span class="leader"></span><span>$1.49 each</span></div>
    </div>
  </section>

  <div class="bottom-rule"></div>
  <footer class="contact-bar">
    <span><b>Catering Director:</b> Dana Whitfield</span>
    <span class="dot">●</span>
    <span><b>P:</b> 555-861-0142</span>
    <span class="dot">●</span>
    <span><b>F:</b> 555-867-0187</span>
    <span class="dot">●</span>
    <span><b>C:</b> 555-795-0163</span>
  </footer>
</main>
</body>
</html>
```